New letter head for Air Conditioning business

We need a new professional letter head design to suit our new re-branded air conditioning business. Our new logo is attached

```html
<!DOCTYPE html>
<html lang="en">
<head>
<meta charset="UTF-8">
<title>Nordvent Letterhead</title>
<link rel="stylesheet" href="https://fonts.googleapis.com/css2?family=Roboto+Condensed:wght@400;700&display=swap">
<style>
  :root {
    --ink: #454b50;
    --green: #45a86f;
    --red: #e0605a;
    --text: #2b2b2b;
    --paper: #ffffff;
    --backdrop-tint: #f1f6f2;
  }
  * { margin: 0; padding: 0; box-sizing: border-box; }
  html, body {
    width: 848px;
    height: 1200px;
    overflow: hidden;
    background: var(--paper);
  }
  .letterhead {
    position: relative;
    width: 848px;
    height: 1200px;
    overflow: hidden;
    background: var(--paper);
    font-family: "Roboto Condensed", "Arial Narrow", sans-serif;
    color: var(--text);
  }
  .backdrop-mark {
    position: absolute;
    left: 0;
    top: 0;
    width: 848px;
    height: 1200px;
    pointer-events: none;
  }
  .brand {
    position: absolute;
    top: 30px;
    left: 0;
    width: 100%;
    display: flex;
    flex-direction: column;
    align-items: center;
  }
  .brand-dot {
    width: 26px;
    height: 26px;
    border-radius: 50%;
    background: var(--green);
    margin-bottom: 20px;
  }
  .brand-name {
    font-weight: 700;
    font-size: 32px;
    line-height: 1;
    letter-spacing: 6px;
    color: var(--ink);
    text-transform: uppercase;
    padding-left: 6px;
  }
  .brand-tagline {
    margin-top: 8px;
    font-weight: 700;
    font-size: 9px;
    letter-spacing: 2px;
    color: var(--green);
    text-transform: uppercase;
  }
  .footer {
    position: absolute;
    left: 0;
    top: 1118px;
    width: 100%;
    text-align: center;
  }
  .footer-rule {
    display: flex;
    width: 510px;
    height: 2px;
    margin: 0 auto;
  }
  .footer-rule span { flex: 1; }
  .footer-rule .rule-ink { background: var(--ink); }
  .footer-rule .rule-green { background: var(--green); }
  .footer-rule .rule-red { background: var(--red); }
  .footer-contact {
    margin-top: 8px;
    font-size: 14px;
    line-height: 17px;
    font-weight: 400;
    color: var(--text);
  }
</style>
</head>
<body>
  <main class="letterhead">
    <svg class="backdrop-mark" viewBox="0 0 848 1200" aria-hidden="true">
      <circle cx="250" cy="870" r="290" fill="var(--backdrop-tint)"/>
    </svg>

    <header class="brand">
      <div class="brand-dot"></div>
      <div class="brand-name">Nordvent</div>
      <div class="brand-tagline">Air Conditioning &amp; Refrigeration</div>
    </header>

    <footer class="footer">
      <div class="footer-rule">
        <span class="rule-ink"></span>
        <span class="rule-green"></span>
        <span class="rule-red"></span>
      </div>
      <p class="footer-contact">
        Add: 12 Street Name, City, State,&nbsp; Country Name | Mob: 00122 987 654 321<br>
        mail: info@nordventmail.com | website: www.nordvent-site.com
      </p>
    </footer>
  </main>
</body>
</html>
```